Get me out of Jail business cards!!!!

I need business cards done for my business. I own a BailBonds and I get people out of jail!

Colors are red white and black

I need it to say on the card these details:

Rollin’ Free Bailbonds

452 S Kettering Ave
Arcadia, FL 34266

863-555-0172

Open 24/7

On the back of the card:

Must check in every Tuesday.

______/______/______ court date
____________________ time
You must know your court date at all times!

Marla Tisdell - owner
Rosalind Tisdell - agent
Denise Crandon - agent

Industry/Entity Type

Bail bonds

Contact Information for Business Card

Colors are red white and black I need it to say on the card these details: Rollin’ Free Bailbonds 452 S Kettering Ave Arcadia, FL 34266 863-555-0172 Open 24/7 On the back of the card: Must check in every Tuesday. ______/______/______ court date ____________________ time You must know your court date at all times! Marla Tisdell - owner Rosalind Tisdell - agent Denise Crandon - agent

Font styles to use
Serif
Sans Serif

Colors
EB3D1F
EC4F4E
F09395
F8D3D4
FCEDEE

Requirements
Must have
• I listed the must haves in the business card details
Nice to have
• Handcuffs or jail bars or a man in a black and white suit

```html
<!DOCTYPE html>
<html lang="en">
<head>
<meta charset="utf-8">
<title>Rollin’ Free Bailbonds – Business Cards</title>
<link rel="stylesheet" href="https://fonts.googleapis.com/css2?family=Roboto+Slab:wght@700;800;900&family=Montserrat:wght@300;400;500&display=swap">
<style>
  :root {
    --page-bg: #989898;
    --card-black: #000000;
    --card-light: #dedede;
    --brand-red: #ff0000;
    --ink: #111111;
    --white: #ffffff;
    --rule: #9a9a9a;
  }
  * { box-sizing: border-box; margin: 0; padding: 0; }
  html, body { width: 1200px; height: 1200px; overflow: hidden; }
  body {
    background: var(--page-bg);
    position: relative;
    font-family: "Montserrat", Arial, sans-serif;
  }
  .card {
    position: absolute;
    left: 201px;
    width: 798px;
    height: 466px;
    overflow: hidden;
  }
  .card--front { top: 84px; background: var(--card-black); }
  .card--back { top: 600px; background: var(--card-light); border: 1px solid #c8c8c8; }

  /* Front */
  .jail-photo {
    position: absolute;
    left: 411px; top: 0;
    width: 375px; height: 180px;
    background: radial-gradient(ellipse at 55% 45%, #6a6a6a 0%, #3a3a3a 35%, #141414 70%, #000 100%);
  }
  .brand-name {
    position: absolute;
    right: 87px; top: 108px;
    text-align: right;
    color: var(--white);
    font-family: "Montserrat", Arial, sans-serif;
    font-weight: 400;
    font-size: 84px;
    line-height: 0.98;
    letter-spacing: -1px;
  }
  .phone {
    position: absolute;
    right: 87px; top: 316px;
    display: flex; align-items: center; gap: 8px;
    color: var(--white);
    font-family: "Roboto Slab", Georgia, serif;
    font-weight: 900;
    font-size: 34px;
    line-height: 1;
  }
  .phone svg { width: 32px; height: 32px; }
  .address {
    position: absolute;
    right: 87px; top: 366px;
    color: var(--white);
    font-size: 16px;
    font-weight: 500;
  }
  .open-band {
    position: absolute;
    left: 416px; top: 401px;
    width: 294px; height: 35px;
    background: linear-gradient(90deg, #000 0%, #fff 22%, #fff 78%, #000 100%);
    color: var(--brand-red);
    font-family: "Roboto Slab", Georgia, serif;
    font-weight: 900;
    font-size: 28px;
    text-align: center;
    line-height: 35px;
  }

  /* Back */
  .checkin-title {
    position: absolute;
    left: 0; right: 0; top: 42px;
    text-align: center;
    color: var(--brand-red);
    font-family: "Roboto Slab", Georgia, serif;
    font-weight: 900;
    font-size: 38px;
    text-shadow: 2px 2px 0 #300;
    padding-left: 30px;
  }
  .staff { position: absolute; right: 426px; top: 138px; text-align: right; }
  .staff-member { margin-bottom: 14px; }
  .staff-name {
    color: var(--brand-red);
    font-family: "Roboto Slab", Georgia, serif;
    font-weight: 800;
    font-size: 28px;
    line-height: 1.05;
  }
  .staff-role { font-size: 16px; color: var(--ink); line-height: 1.1; }
  .divider-vertical {
    position: absolute; left: 399px; top: 132px;
    width: 1px; height: 200px; background: var(--rule);
  }
  .fill-in { position: absolute; text-align: center; color: var(--ink); font-size: 19px; }
  .fill-in--date { left: 440px; top: 172px; width: 260px; }
  .fill-in--time { left: 434px; top: 236px; width: 272px; }
  .date-line { display: flex; justify-content: space-between; align-items: flex-end; height: 22px; color: var(--rule); }
  .date-line span.blank { flex: 1; border-bottom: 1.5px solid var(--rule); height: 100%; }
  .time-line { border-bottom: 1.5px solid var(--rule); height: 28px; line-height: 20px; color: var(--ink); }
  .reminder {
    position: absolute; left: 0; right: 0; top: 348px;
    text-align: center; font-size: 20px; color: var(--ink);
  }
  .divider-horizontal {
    position: absolute; left: 21px; right: 23px; top: 392px;
    height: 1.5px; background: var(--rule);
  }
  .footer-name {
    position: absolute; left: 0; right: 0; top: 408px;
    text-align: center;
    color: var(--brand-red);
    font-family: "Roboto Slab", Georgia, serif;
    font-weight: 800;
    font-size: 30px;
  }
</style>
</head>
<body>
  <section class="card card--front">
    <div class="jail-photo" role="img" aria-label="Photo of two hands gripping jail cell bars"></div>
    <h1 class="brand-name">Rollin’ Free<br>Bailbonds</h1>
    <div class="phone">
      <svg viewBox="0 0 32 32" aria-hidden="true">
        <circle cx="16" cy="16" r="16" fill="var(--brand-red)"/>
        <path d="M11 8c1 0 2.5 3 2.5 4s-1.5 1.5-1.3 2.5c.6 2 2.3 3.7 4.3 4.3 1 .2 1.5-1.3 2.5-1.3s4 1.5 4 2.5-1.5 3-3 3C13.5 23.5 8.5 18.5 8.5 11.5 8.5 10 10 8 11 8z" fill="var(--white)"/>
      </svg>
      <span>863•555•0172</span>
    </div>
    <p class="address">452 S Kettering Ave, Arcadia, FL 34266</p>
    <div class="open-band">OPEN 24/7</div>
  </section>

  <section class="card card--back">
    <h2 class="checkin-title">Must check in every Tuesday!</h2>
    <div class="staff">
      <div class="staff-member"><div class="staff-name">Marla Tisdell</div><div class="staff-role">OWNER</div></div>
      <div class="staff-member"><div class="staff-name">Rosalind Tisdell</div><div class="staff-role">AGENT</div></div>
      <div class="staff-member"><div class="staff-name">Denise Crandon</div><div class="staff-role">AGENT</div></div>
    </div>
    <div class="divider-vertical"></div>
    <div class="fill-in fill-in--date">
      <div class="date-line"><span class="blank"></span>/<span class="blank"></span>/<span class="blank"></span></div>
      <div>court date</div>
    </div>
    <div class="fill-in fill-in--time">
      <div class="time-line">:</div>
      <div>time</div>
    </div>
    <p class="reminder">You must know your court date at all times!</p>
    <div class="divider-horizontal"></div>
    <div class="footer-name">Rollin’ Free Bailbonds</div>
  </section>
</body>
</html>
```